Crestline Folio Network Presents… CFNMerit.example

I. The purpose of the phase1 is to gain access to (and control of) scholastic academic works that had been written and authored by students, but only after they have been corrected (vetted), by education professionals and returned to the student as corrected documents. It is my goal to push the CFN Merit Annual as inducements to have students turn over these papers and receive recognition and authorship, for these intellectual works.

Target Market(s)

university students
high school students

Number of Pages Required

2 page

Font styles to use
Serif
Sans Serif

Colors

Designer to choose colors to be used in the design.

Requirements
Must have
• must include this or similar language.
• Crestline Folio Network Presents…
• CFNMerit.example
• Here is the assemblage of your academic successes. We collect and archive your written academic achievements, you’re “A” graded as correct, written assignments throughout the year, and when it’s over, we amass your academic documents into a bound book… your Scholar Summit Annual.
• You study hard and work hard all year trying to achieve the highest grades possible. At the end of the year, semester, or term you will have lasting proof to show what you did to achieve your academic excellence… and in book form too!
• Consider this the perfect gift to yourself to celebrate your ascendency and to showcase all of the hard work that you have put into getting to the next step on the ladder to success, your success.
• One good thing about this is that you don’t have to do any extra work to write your book. Once your written assignment has been reviewed, graded by an education authority and returned to you, all you do is to submit it to your registered account with us, add a brief description or special detail and we will add it to your database to build your success story.
• Our mission here is to track and highlight your academic successes. We want to honor and immortalize you through your academic “A” papers. Currently, once your term papers, research papers, writing assignments, book reports, studies, critiques, essays, theses, dissertations and the like, have been graded and returned back to you they soon become of no further value to you. But now with the Scholar Summit Annual you have a system available to you that can and will create a lasting record or Yearbook to catalogue what molded you into the intellectual that you have become. Once your academic papers have been evaluated by the scholastic authority and graded accordingly, you only have to post or download these materials as they become available to you. As you repeat the process again and again the storehouse of your knowledge legacy grows exponentially and become more relevant and valuable as entries into your Scholar Summit Annual.
• Imagine if you will, if there was a written record of Kowalczyk’s early studies and writings, from before he became the Kowalczyk that we know of today, or the Pemberton’s early school and college writings? Just think of the value that these priceless gifts would hold today. Well you may say “but I’m not famous. Who would be interested in my schoolwork or assignments?” We can’t say for sure right now because the future is not known today. But we do know that years of study and research molded and shaped the Pembertons from their modest upbringing and that Kowalczyk struggled for many years trying to get his thoughts and writings accepted by the establishment before they finally realized that “e” really did equal “mc2” (e=mc2). Who Knew? But you don’t have to become famous to be relevant. What value would you place on old mementos and writings of your parents, grand or great grandparents from before Vietnam or WWIl or??? I’m sure Kinroot.example would kill to have access to these treasures. And so would your kids or descendants in future years. Yes, you are relevant and you can make a lasting difference if you create an enduring legacy. Together we can create that legacy.
• “Log on to: CFNMerit.example to comprehend what all the excitement is all about.”
• We are the vehicle to deliver your curriculum based study writings to you in the easiest and most hassle free way possible. As members of the Scholar Summit community your papers will always be available to you. Periodically this material will be compiled, configured if necessary, and formatted into book form as your personalized Scholar Summit Annual matures.
Nice to have
• very professional but student friendly graphes
Should not have
• leave out the affiliate program at this time.

```html
<!DOCTYPE html>
<html lang="en">
<head>
<meta charset="utf-8">
<title>CFNMerit.example</title>
<link href="https://fonts.googleapis.com/css2?family=Montserrat:wght@500;600;700;800&family=Open+Sans:wght@400;600;700&display=swap" rel="stylesheet">
<style>
  :root {
    --green: #1f9a4b;
    --green-dark: #17803c;
    --navy: #0d1a30;
    --navy-deep: #08111f;
    --ink: #2c3a4a;
    --blue-text: #2f6fc4;
    --white: #ffffff;
    --hero-top: #3c4147;
    --hero-bottom: #1d2125;
    --rule: #d9dde2;
  }
  * { box-sizing: border-box; margin: 0; padding: 0; }
  html, body { width: 1200px; height: 3196px; overflow: hidden; }
  body {
    position: relative;
    background: var(--white);
    font-family: "Open Sans", Arial, sans-serif;
    color: var(--ink);
  }
  .hero {
    position: absolute; left: 0; top: 0; width: 1200px; height: 760px;
    background: linear-gradient(160deg, #555a60 0%, var(--hero-top) 35%, var(--hero-bottom) 100%);
  }
  .nav {
    position: absolute; top: 44px; left: 0; width: 1200px; height: 50px;
  }
  .brand {
    position: absolute; left: 22px; top: 0;
    font-family: "Montserrat", Arial, sans-serif; font-weight: 700;
    font-size: 36px; color: var(--white); letter-spacing: 0.2px;
  }
  .nav-links { position: absolute; top: 22px; left: 0; width: 1200px; list-style: none; }
  .nav-links li {
    position: absolute; font-family: "Montserrat", Arial, sans-serif;
    font-weight: 500; font-size: 18px; color: var(--white); white-space: nowrap;
  }
  .hero-title {
    position: absolute; top: 262px; left: 0; width: 1200px; text-align: center;
    font-family: "Montserrat", Arial, sans-serif; font-weight: 800;
    font-size: 62px; color: var(--white); letter-spacing: 0.3px;
  }
  .search {
    position: absolute; left: 408px; top: 398px; width: 480px; height: 56px;
    background: var(--white); border-radius: 28px;
  }
  .search-placeholder {
    position: absolute; left: 28px; top: 16px; font-size: 16px; color: #9aa1a8;
  }
  .search-btn {
    position: absolute; right: 4px; top: 4px; width: 48px; height: 48px;
    border-radius: 50%; background: var(--green);
  }
  .search-btn svg { position: absolute; left: 12px; top: 12px; }
  .dots { position: absolute; top: 574px; left: 544px; width: 112px; height: 20px; }
  .dot { position: absolute; top: 0; width: 20px; height: 20px; border-radius: 50%; background: var(--white); }
  .dot.active { background: var(--green); }

  .card {
    position: absolute; background: var(--white);
    box-shadow: 0 6px 26px rgba(0,0,0,0.18);
  }
  .intro-card { left: 240px; top: 636px; width: 720px; height: 440px; padding: 56px 60px 0; text-align: center; }
  .card-title {
    font-family: "Montserrat", Arial, sans-serif; font-weight: 700;
    font-size: 40px; color: var(--green);
  }
  .card-rule { width: 480px; height: 2px; background: var(--rule); margin: 14px auto 30px; }
  .intro-card p { font-size: 18px; line-height: 34px; color: var(--blue-text); }

  .achievements { position: absolute; top: 1150px; left: 0; width: 1200px; text-align: center; }
  .section-title {
    font-family: "Montserrat", Arial, sans-serif; font-weight: 700;
    font-size: 52px; color: var(--green);
  }
  .section-rule { width: 680px; height: 2px; background: var(--green); margin: 18px auto 30px; }
  .achievements p { width: 1010px; margin: 0 auto; font-size: 18px; line-height: 34px; color: var(--blue-text); }

  .how { position: absolute; top: 1450px; left: 0; width: 1200px; height: 800px; }
  .how svg { position: absolute; left: 0; top: 0; }
  .how-title {
    position: absolute; top: 240px; left: 0; width: 1200px; text-align: center;
    font-family: "Montserrat", Arial, sans-serif; font-weight: 600;
    font-size: 70px; color: var(--white);
  }
  .how-text {
    position: absolute; top: 400px; left: 120px; width: 960px; text-align: center;
    font-size: 18px; line-height: 34px; color: var(--white);
  }

  .vehicle-card { left: 248px; top: 2276px; width: 840px; height: 250px; padding: 30px 40px 0; text-align: center; }
  .vehicle-card p { font-size: 16px; line-height: 31px; font-weight: 700; color: var(--blue-text); }

  .cta {
    position: absolute; left: 316px; top: 2596px; width: 648px; height: 92px;
    border-radius: 46px; background: var(--green);
    font-family: "Montserrat", Arial, sans-serif; font-weight: 700; font-size: 28px;
    color: var(--white); text-align: center; line-height: 92px;
  }

  .footer { position: absolute; top: 2776px; left: 0; width: 1200px; height: 420px; background: var(--navy); }
  .footer-col { position: absolute; top: 40px; color: var(--white); }
  .footer-col h3 {
    font-family: "Montserrat", Arial, sans-serif; font-weight: 500;
    font-size: 19px; letter-spacing: 0.5px; margin-bottom: 16px;
  }
  .footer-rule { width: 170px; height: 1px; background: rgba(255,255,255,0.35); margin-bottom: 22px; }
  .footer-col ul { list-style: none; }
  .footer-col li { font-size: 19px; line-height: 29px; }
  .bottom-bar {
    position: absolute; left: 0; bottom: 0; width: 1200px; height: 56px;
    background: var(--navy-deep); color: #c7ced8; font-size: 15px;
  }
  .copyright { position: absolute; left: 22px; top: 18px; }
  .legal { position: absolute; right: 22px; top: 18px; }
</style>
</head>
<body>

<header class="hero" role="img" aria-label="Photograph of a student studying with books, darkened behind the headline">
  <nav class="nav">
    <div class="brand">CFNMerit.example</div>
    <ul class="nav-links">
      <li style="left:606px">Home</li>
      <li style="left:702px">About Us</li>
      <li style="left:846px">What we do</li>
      <li style="left:992px">Sign Up</li>
      <li style="left:1116px">Login</li>
    </ul>
  </nav>
  <h1 class="hero-title">We put the profit in Learning</h1>
  <div class="search">
    <span class="search-placeholder">Type text to search</span>
    <span class="search-btn">
      <svg width="24" height="24" viewBox="0 0 24 24"><path d="M8 4 L16 12 L8 20" fill="none" stroke="#fff" stroke-width="3.5" stroke-linecap="round" stroke-linejoin="round"/></svg>
    </span>
  </div>
  <div class="dots">
    <span class="dot active" style="left:0"></span>
    <span class="dot" style="left:46px"></span>
    <span class="dot" style="left:92px"></span>
  </div>
</header>

<section class="card intro-card">
  <h2 class="card-title">What CFNMerit Do</h2>
  <div class="card-rule"></div>
  <p>We collect and archive your written academic achievements, you’re “A” graded as correct, written assignments throughout the year, and when it’s over, we amass your academic documents into a bound book… your CFN Merit Annual.</p>
</section>

<section class="achievements">
  <h2 class="section-title">Track you annual Achievements</h2>
  <div class="section-rule"></div>
  <p>You study hard and work hard all year trying to achieve the highest grades possible. At the end of the year, semester, or term you will have lasting proof to show what you did to achieve your academic excellence… and in book form too!<br>Consider this the perfect gift to yourself to celebrate your ascendency and to showcase all of the work that you have put into getting to the next step on the ladder to success, your success.</p>
</section>

<section class="how">
  <svg width="1200" height="800" viewBox="0 0 1200 800" aria-hidden="true">
    <defs>
      <linearGradient id="howShade" x1="0" y1="0" x2="1" y2="1">
        <stop offset="0" stop-color="#2a2f33"/>
        <stop offset="0.5" stop-color="#4a4f52"/>
        <stop offset="1" stop-color="#1c2024"/>
      </linearGradient>
    </defs>
    <polygon points="0,100 600,10 1200,100 1200,600 600,735 0,600" fill="var(--green)"/>
    <polygon points="0,100 600,10 1200,100 1200,582 600,712 0,582" fill="url(#howShade)" role="img" aria-label="Photograph of a student writing at a desk"/>
  </svg>
  <h2 class="how-title">How it works</h2>
  <p class="how-text">One good thing about this is that you don’t have to do any extra work to write your book. Once your written assignment has been reviewed, graded by an education authority and returned to you, all you do is to submit it to your registered account with us, add a brief description or special detail and we will add it to your database to build your success story.</p>
</section>

<section class="card vehicle-card">
  <p>We are the vehicle to deliver your curriculum based study writings to you in the easiest and most hassle free way possible. Log on to comprehend what all the excitement is all about.<br>As a member of the Scholar Summit community your papers will always be available to you. Periodically this material will be compiled, edited if necessary, and formatted into book form as your personalized CFN Merit Annual matures.</p>
</section>

<div class="cta">Get Your CFN Merit Annual Now</div>

<footer class="footer">
  <div class="footer-col" style="left:80px">
    <h3>QUICK LINKS</h3>
    <div class="footer-rule"></div>
    <ul><li>Home</li><li>About Us</li><li>Services</li><li>News</li></ul>
  </div>
  <div class="footer-col" style="left:332px">
    <h3>CONTACT US</h3>
    <div class="footer-rule"></div>
    <ul><li>Email: hello@cfnmerit.example</li><li>Tel: (020) 5550 0192</li><li>Street: 14 Quarry Lane, Millbrook</li></ul>
  </div>
  <div class="footer-col" style="left:920px">
    <h3>LOCATION MAP</h3>
  </div>
  <div class="bottom-bar">
    <span class="copyright">Copyright © 2018 Crestline Folio Network. All rights reserved</span>
    <span class="legal">Terms Of Service | Privacy Policy</span>
  </div>
</footer>

</body>
</html>
```